Please make an eye catching and elegant flyer. Here is the content
Lorena's 70th Birthday Bash
Friday September 13th, 2024
8pm - 12midnight
Location:
Pelbrook's Oakland
47 Marlow St, Oakland, CA 94618
For more information and to RSVP contact 916-482-3157 or 510-647-2083

Colors
FFF300
FFF600
FEFA6F
FFFEC7
FFFEE8
EB3D1F
EC4F4E
F09395
F8D3D4
FCEDEE
A7469A
B969AE
D3A5CF
EDDBEB
F8F0F9

Requirements
Nice to have
• Her favorite colors are royal purple, white, red. and gold. You don't have to use all of these colors yet at least a couple would be nice.

```html
<!DOCTYPE html>
<html lang="en">
<head>
<meta charset="utf-8">
<title>Lorena's 70th Birthday Bash</title>
<link rel="stylesheet" href="https://fonts.googleapis.com/css2?family=Anton&family=Montserrat:wght@600;700;800;900&display=swap">
<style>
  :root {
    --page-bg: #3b3634;
    --paper: #fbf6f8;
    --royal-purple: #4a0f7a;
    --title-purple: #4b1486;
    --party-red: #e3161f;
    --gold-band: #f1d472;
    --gold-text: #f5c842;
    --ink: #1b1b1b;
    --white: #ffffff;
    --balloon-blue: #2f6fd6;
    --balloon-violet: #a23bd0;
    --dress-red: #d3141c;
    --wrap-dark: #3a2b1c;
  }
  * { margin: 0; padding: 0; box-sizing: border-box; }
  html, body { width: 1200px; height: 800px; overflow: hidden; }
  body {
    background: var(--page-bg);
    display: flex;
    align-items: center;
    justify-content: center;
    font-family: "Montserrat", Arial, sans-serif;
  }
  .flyer {
    position: relative;
    width: 560px;
    height: 780px;
    background: var(--paper);
    overflow: hidden;
    box-shadow: 0 10px 30px rgba(0,0,0,.45);
  }
  .bunting {
    position: absolute; left: 0; top: 0; width: 360px; height: 78px;
    background: linear-gradient(90deg, #5aa6b8, #f08a3c, #6fb548, #a6359a, #e3261f, #5aa6b8);
    opacity: .85;
    clip-path: polygon(0 0, 100% 0, 100% 35%, 0 100%);
  }
  .cake {
    position: absolute; right: 50px; top: 14px; width: 110px; height: 90px;
    border-radius: 14px;
    background: linear-gradient(180deg, #f5a7cf, #8fd0e8);
  }
  .title { position: absolute; left: 34px; top: 92px; line-height: 1; font-family: "Anton", Impact, sans-serif; }
  .title__name {
    display: block; font-size: 46px; color: var(--title-purple);
    text-shadow: 2px 2px 0 #d9cfe6; letter-spacing: 1px;
  }
  .title__event {
    display: block; font-size: 80px; color: var(--party-red);
    text-shadow: 3px 3px 0 #f3c9cb; letter-spacing: 1px; margin-top: 4px;
  }
  .balloons {
    position: absolute; left: 38px; top: 248px; width: 190px; height: 190px;
    border-radius: 50%;
    background: radial-gradient(circle at 40% 35%, var(--balloon-violet), var(--balloon-blue) 70%);
    z-index: 2;
  }
  .date-band {
    position: absolute; left: 0; top: 428px; width: 340px; height: 172px;
    background: var(--gold-band);
  }
  .portrait {
    position: absolute; right: 0; top: 236px; width: 264px; height: 430px;
    background: linear-gradient(180deg, var(--wrap-dark) 0%, #6b4a35 28%, var(--dress-red) 48%, #b0101a 100%);
    z-index: 1;
  }
  .date { position: absolute; left: 30px; top: 440px; z-index: 3; }
  .date__row { display: flex; align-items: flex-end; gap: 10px; }
  .date__day {
    font-family: "Anton", Impact, sans-serif; font-size: 72px; line-height: .95; color: var(--ink);
  }
  .date__weekday {
    background: var(--party-red); color: var(--white);
    font-weight: 800; font-size: 26px; padding: 4px 12px; margin-bottom: 40px;
  }
  .date__month { font-weight: 900; font-size: 27px; color: var(--ink); margin-top: 4px; }
  .date__time { font-weight: 700; font-size: 25px; color: var(--title-purple); margin-top: 2px; }
  .venue { position: absolute; left: 40px; top: 610px; font-size: 16px; line-height: 20px; color: var(--ink); }
  .venue__label { color: var(--party-red); font-weight: 900; text-decoration: underline; }
  .venue__name { font-weight: 800; }
  .venue__address { font-weight: 600; }
  .contact-band {
    position: absolute; left: 0; bottom: 0; width: 560px; height: 140px;
    background: var(--royal-purple);
    clip-path: polygon(0 57%, 100% 0, 100% 100%, 0 100%);
    z-index: 2;
  }
  .contact {
    position: absolute; left: 40px; bottom: 8px; z-index: 3;
    color: var(--white); font-weight: 800; font-size: 17px; line-height: 23px;
  }
  .contact__phone { color: var(--gold-text); }
</style>
</head>
<body>
  <main class="flyer">
    <div class="bunting" role="img" aria-label="Colorful party bunting flags with streamers"></div>
    <div class="cake" role="img" aria-label="Illustration of a pink and blue tiered birthday cake with candles"></div>

    <h1 class="title">
      <span class="title__name">LORENA'S 70TH</span>
      <span class="title__event">BIRTHDAY BASH</span>
    </h1>

    <div class="date-band"></div>
    <div class="balloons" role="img" aria-label="Bunch of shiny blue and purple balloons"></div>
    <div class="portrait" role="img" aria-label="Photo of the birthday celebrant in a red lace outfit and head wrap"></div>

    <section class="date">
      <div class="date__row">
        <span class="date__day">13th</span>
        <span class="date__weekday">FRIDAY</span>
      </div>
      <p class="date__month">SEPTEMBER, 2024</p>
      <p class="date__time">8PM - 12MIDNIGHT</p>
    </section>

    <address class="venue" style="font-style:normal">
      <span class="venue__label">LOCATION:</span><br>
      <span class="venue__name">Pelbrook's Oakland</span><br>
      <span class="venue__address">47 Marlow St, Oakland,<br>CA 94618</span>
    </address>

    <div class="contact-band"></div>
    <p class="contact">
      For more information and<br>
      to RSVP contact <span class="contact__phone">916-482-3157</span><br>
      or <span class="contact__phone">510-647-2083</span>
    </p>
  </main>
</body>
</html>
```